Tuition Center Website

We need a new web site for a tutoring company based in sydney.

We only teach senior highschool students and pride ourselves on building the students abilities to think their way through life.

I would like a bright and vibrant website that looks professional and modern.
It needs to look simple and neat but also have the functionality we need.
Images and flash would be good.

Please keep in mind that the site must be appealing to a younger audience.

We need a multipage website with the following navigation bars:

1.Home (As logo not "home" button)
I would like a news box/ticker somewhere that can stream our chatterbook and peeplr feeds and also any news updates we want to put up.
Subscribe to newsletter button.

2. About us.
This needs to be a pull down into:
-What we do
-Why we do it
-How we do it

3. Courses
Pulldown into:
-Maths
-English
-Science
(we may need to attach extra pages behind these e.g. Courses/Science/Physics or Courses/Science/Chemistry and possibly add a link to a new formvik form)

4. Inspired
This page is like a blog page where we can upload videos, links to articles that we find to be inspiring and hopefully will inspire others.

5. Inspire
This is a recruitment page. Only content here.

6. Contact us.
Trovix map widget and a 'contact us' form

* Our branding requires green close to #12FF3D

***Please have a look at the current website.
@ www.velmoralearning.com.au

Thanks everybody hope the revision of my brief is better and more informative than my last one
Updates

Target Market(s)

senior highschool students aged 15-19, parents ( to a lesser degree)

Industry/Entity Type

It Company

Requirements
Must have
• Ability to change content on pages.

The green doesn't have to be everywhere, but it must be obvious that it is our colour.

Nice to have
• Sites with a nicer mix of images and flash will be given more consideration. But then again, if you amaze us, you amaze us and we will go with your design.
Should not have
• Should stay away from ocre, brown colours and serif fonts.

```html
<!DOCTYPE html>
<html lang="en">
<head>
<meta charset="utf-8">
<title>Velmora Learning – HSC Tutoring</title>
<link rel="stylesheet" href="https://fonts.googleapis.com/css2?family=Open+Sans:wght@300;400;600;700&family=Asap+Condensed:wght@600&family=Indie+Flower&family=Righteous&display=swap">
<style>
:root{
  --page-green:#88c541;
  --frame-white:#ffffff;
  --cream:#f4f7e6;
  --nav-dark:#0e4a1f;
  --nav-mid:#1c6b2b;
  --brand-green:#12ff3d;
  --hero-top:#7fd62a;
  --hero-bottom:#1f7a2e;
  --hero-edge:#b9e87a;
  --deep-green:#0c3417;
  --news-green:#1e6b2f;
  --news-lime:#9cf04a;
  --ink:#1d1d1d;
  --slate:#4f6c74;
  --muted-ink:#55604a;
}
*{box-sizing:border-box;margin:0;padding:0}
html,body{width:1200px;height:1061px;overflow:hidden}
body{background:var(--page-green);font-family:"Open Sans",Arial,sans-serif;color:var(--ink);position:relative}
.site-frame{position:absolute;left:137px;top:43px;width:923px;height:873px;background:var(--frame-white);border-radius:9px}
.site{position:absolute;left:5px;top:5px;width:913px;height:863px;background:var(--cream);border-radius:6px;overflow:hidden}
/* header */
.brand{position:absolute;left:58px;top:10px;display:flex;align-items:center;gap:8px}
.brand-mark{width:40px;height:40px;background:var(--brand-green)}
.brand-name{font-weight:700;font-size:19px;line-height:1.05;color:var(--nav-dark);text-transform:lowercase}
.skyline{position:absolute;left:522px;top:42px;width:391px;height:46px;background:linear-gradient(to top,#e1ebc6,#eef3da 80%,transparent)}
.contact{position:absolute;left:590px;top:29px;font-size:12.5px;font-style:normal;line-height:20px;color:var(--muted-ink)}
/* nav */
.main-nav{position:absolute;left:0;top:92px;width:913px;height:39px;background:linear-gradient(var(--nav-mid),var(--nav-dark))}
.main-nav a{position:absolute;top:0;height:39px;line-height:39px;color:#fff;font-weight:700;font-size:13px;text-decoration:none;transform:translateX(-50%);white-space:nowrap}
.main-nav a.active{left:0;transform:none;width:81px;text-align:center;background:linear-gradient(#4f9d44,#2f7a30);color:#143b17}
/* hero */
.hero-intro{position:absolute;left:0;top:135px;width:402px;height:320px;background:linear-gradient(var(--hero-top),var(--hero-bottom));border-right:8px solid var(--hero-edge)}
.hero-intro h1{position:absolute;left:40px;top:28px;font-weight:300;font-size:35px;color:#fff;white-space:nowrap}
.hero-intro p{position:absolute;left:41px;top:80px;width:340px;font-size:13px;line-height:26px;color:#0d260f;white-space:nowrap}
.btn-enquire{position:absolute;left:142px;top:237px;width:231px;height:38px;border-radius:10px;background:var(--deep-green);color:#e6f5d8;font-size:14px;line-height:38px;text-align:center;text-decoration:none}
.hero-photo{position:absolute;left:412px;top:135px;width:501px;height:320px;background:linear-gradient(#8592a6 0%,#a4acb6 35%,#8a6b4e 60%,#6a7a4a 85%,#a58f6a 100%)}
/* lower columns */
.news-tab{position:absolute;left:25px;top:477px;width:176px;height:36px;background:var(--deep-green);border-radius:8px 8px 0 0;color:var(--news-lime);font-size:19px;line-height:36px;padding-left:14px}
.news-box{position:absolute;left:25px;top:513px;width:259px;height:290px;background:var(--news-green);border-radius:0 8px 8px 8px}
.news-item{position:absolute;left:17px;width:225px}
.news-thumb{height:85px}
.news-item h3{font-size:12px;font-weight:700;color:#fff;margin-top:7px}
.btn-more{position:absolute;left:88px;top:277px;width:150px;height:24px;border-radius:10px;background:var(--deep-green);color:var(--news-lime);font-size:12px;line-height:24px;text-align:center;text-decoration:none;box-shadow:2px 3px 5px rgba(0,0,0,.35)}
.col-title{position:absolute;font-family:"Asap Condensed","Arial Narrow",sans-serif;font-weight:600;color:#000;white-space:nowrap}
.col-title span{color:var(--page-green)}
.col-photo{position:absolute;width:253px;height:134px;border:1px solid var(--news-green);border-radius:8px;padding:3px;background:#fff}
.col-photo div{width:100%;height:100%;border-radius:6px}
.col-text{position:absolute;font-size:12.5px;line-height:19.5px;color:#111;white-space:nowrap}
.signature{position:absolute;left:421px;top:764px;font-family:"Indie Flower",cursive;font-size:13px;color:#333}
.btn-send{position:absolute;left:641px;top:771px;width:154px;height:29px;border-radius:9px;background:var(--slate);color:#fff;font-weight:700;font-size:12.5px;line-height:29px;text-align:center;text-decoration:none}
/* footer */
.foot-nav a{position:absolute;top:928px;font-family:"Righteous",sans-serif;font-size:12.5px;color:#fff;text-decoration:none;text-transform:uppercase;transform:translateX(-50%);white-space:nowrap}
.foot-nav a.active{color:#000}
.foot-rule{position:absolute;left:199px;top:954px;width:805px;height:5px;background:linear-gradient(#9aa4a8,#5b6a78)}
.copyright{position:absolute;left:0;width:1200px;top:1002px;text-align:center;font-size:10.5px;color:#fff;letter-spacing:.3px}
</style>
</head>
<body>
<div class="site-frame">
  <div class="site">
    <header>
      <div class="brand"><span class="brand-mark"></span><span class="brand-name">velmora<br>learning</span></div>
      <div class="skyline" role="img" aria-label="Faint city skyline silhouette"></div>
      <address class="contact">
        Street: 48 Larkin St Ashfield NSW 2131<br>
        Phone: (02) 5550 1457<br>
        Email: learn@velmoralearning.com.au
      </address>
    </header>
    <nav class="main-nav">
      <a class="active" href="#">HOME</a>
      <a href="#" style="left:175px">ABOUT US</a>
      <a href="#" style="left:322px">COURSES</a>
      <a href="#" style="left:470px">INSPIRED</a>
      <a href="#" style="left:617px">INSPIRE</a>
      <a href="#" style="left:780px">CONTACT US</a>
    </nav>
    <section class="hero-intro">
      <h1>I Am Velmora.</h1>
      <p>The HSC help you need, in the years you need it.<br>We offer small classes, individualised attention<br>and genuine care for each student. It's different -<br>in a good way. Feel free to find out more about us,<br>and let us know if there's any way we can help you<br>on your journey.</p>
      <a class="btn-enquire" href="#">ENQUIRE NOW&gt;&gt;</a>
    </section>
    <div class="hero-photo" role="img" aria-label="Row of brick townhouses with gardens under a cloudy sky"></div>

    <div class="news-tab">RECENT NEWS</div>
    <section class="news-box">
      <article class="news-item" style="top:20px">
        <div class="news-thumb" role="img" aria-label="Palm trees in front of apartments at sunset" style="background:linear-gradient(#2a3d6a,#e07a2a 75%,#c45a1e)"></div>
        <h3>Year 11 FREE HSC Workshops!</h3>
      </article>
      <article class="news-item" style="top:146px">
        <div class="news-thumb" role="img" aria-label="University residential tower beside a bridge" style="background:linear-gradient(#9fb9d6,#d8b58a 60%,#6c7a5a)"></div>
        <h3>Uni Open Days 2012</h3>
      </article>
      <a class="btn-more" href="#">View More News&gt;&gt;</a>
    </section>

    <h2 class="col-title" style="left:338px;top:480px;font-size:17px"><span>What Our</span> Students Say</h2>
    <div class="col-photo" style="left:329px;top:513px"><div role="img" aria-label="Students and a tutor working together at a laptop" style="background:linear-gradient(#c9d2d8,#6f7e8e 60%,#39414d)"></div></div>
    <p class="col-text" style="left:330px;top:655px">I like the support the most, how the<br>people and teachers here pick you off<br>your feet, make you do better and tell<br>you that it's not the end of the world!!</p>
    <p class="signature">~Tamsin, Northbrook Girls HS</p>

    <h2 class="col-title" style="left:633px;top:482px;font-size:14px"><span>Ask for your</span> free trial lesson</h2>
    <div class="col-photo" style="left:626px;top:513px"><div role="img" aria-label="Hands holding building plans in front of a construction site" style="background:linear-gradient(#6f9ad0,#c9cfd4 45%,#b9865e)"></div></div>
    <p class="col-text" style="left:629px;top:655px">Because we believe you shouldn't have<br>to sign up until you see what it's actually<br>like. Call or email us now!</p>
    <a class="btn-send" href="#">Send an Enquiry&gt;&gt;</a>
  </div>
</div>

<nav class="foot-nav">
  <a class="active" href="#" style="left:168px">HOME</a>
  <a href="#" style="left:310px">ABOUT US</a>
  <a href="#" style="left:459px">COURSES</a>
  <a href="#" style="left:608px">INSPIRED</a>
  <a href="#" style="left:757px">INSPIRE</a>
  <a href="#" style="left:920px">CONTACT US</a>
</nav>
<div class="foot-rule"></div>
<p class="copyright">© 2013 velmora learning | HSC tutoring &amp; mentoring</p>
</body>
</html>
```